Business card for Mortgage broker business

I have already had the logo designed and am needing a great looking business card. My business focus is on servicing clients who may not be able to obtain finance through traditional lenders due to bad credit, short term employment or they just don't fit the banks profile. It needs to be professional, trust worthy but also have a caring fell about it.
I have provided files showing the green and black logo, the white logo(on white background so the file looks blank) and also a file with the white logo with a background of leaves that was made up which will probably be used for a website header.

Industry/Entity Type

Finance

Contact Information for Business Card

Marcus Dalby
Managing Director, Accredited Finance Broker(AFB)
Po Box 817, Pakenham VIC 3810
marcus@kestrelfunding.com.au
www.kestrelfunding.com.au
0438 216 507

Requirements
Nice to have
• I have added a picture of myself as I would like to see some designs with the pic in it, but I'm not sure if I want it on there with the logo's or just the logo's

```html
<!DOCTYPE html>
<html lang="en">
<head>
<meta charset="utf-8">
<title>Kestrel Funding – Business Card</title>
<link href="https://fonts.googleapis.com/css2?family=Montserrat:wght@400;600;700&display=swap" rel="stylesheet">
<style>
  :root {
    --page-bg: #e4e8e7;
    --card-light: #f5f6f4;
    --card-dark: #1e2828;
    --stripe-light: #c9d0ce;
    --brand-green: #1f6b3a;
    --text-light: #ffffff;
    --icon-ring: #5a6262;
    --icon-fill: #f3f4f2;
  }
  html, body {
    margin: 0;
    padding: 0;
    width: 1200px;
    height: 900px;
    overflow: hidden;
    background: var(--page-bg);
  }
  .canvas {
    position: relative;
    width: 1200px;
    height: 900px;
  }
  .business-card {
    position: absolute;
    left: 120px;
    top: 177px;
    width: 960px;
    height: 548px;
    box-shadow: 0 18px 40px rgba(0, 0, 0, 0.18);
  }
  .card-name {
    font-family: "Montserrat", sans-serif;
    font-weight: 700;
    font-size: 36px;
    fill: var(--text-light);
  }
  .contact-text {
    font-family: "Montserrat", sans-serif;
    font-weight: 400;
    font-size: 19px;
    fill: var(--text-light);
  }
  .brand-name {
    font-family: "Montserrat", sans-serif;
    font-weight: 600;
    font-size: 25px;
    fill: var(--brand-green);
  }
  .icon-ring { fill: var(--icon-fill); stroke: var(--icon-ring); stroke-width: 4; }
  .icon-glyph { fill: var(--brand-green); }
  .icon-line { fill: none; stroke: var(--brand-green); stroke-width: 3; stroke-linecap: round; }
</style>
</head>
<body>
<main class="canvas">
  <svg class="business-card" viewBox="0 0 748 427" xmlns="http://www.w3.org/2000/svg" aria-label="Kestrel Funding business card">
    <!-- card base -->
    <rect class="card-base" x="0" y="0" width="748" height="427" fill="var(--card-light)"/>

    <!-- angled dark panel with accent stripes -->
    <polygon class="accent-stripe-dark" points="296,0 306,0 408,427 398,427" fill="var(--card-dark)"/>
    <polygon class="accent-stripe-light" points="306,0 312,0 414,427 408,427" fill="var(--stripe-light)"/>
    <polygon class="info-panel" points="312,0 748,0 748,427 414,427" fill="var(--card-dark)"/>

    <!-- brand -->
    <g class="brand">
      <circle cx="40" cy="331" r="12" fill="var(--brand-green)"/>
      <text class="brand-name" x="62" y="340">Kestrel Funding</text>
    </g>

    <!-- holder name -->
    <text class="card-name" x="370" y="151">Marcus Dalby</text>

    <!-- phone -->
    <g class="contact-phone">
      <circle class="icon-ring" cx="356" cy="220" r="25"/>
      <path class="icon-glyph" d="M344 214 q12 -8 24 0 l-2 5 h-5 l-1 -3 q-4 -1 -8 0 l-1 3 h-5 z"/>
      <rect class="icon-glyph" x="346" y="220" width="20" height="10" rx="2"/>
      <text class="contact-text" x="398" y="227">0438 216 507</text>
    </g>

    <!-- email -->
    <g class="contact-email">
      <circle class="icon-ring" cx="373" cy="287" r="25"/>
      <rect class="icon-glyph" x="361" y="279" width="24" height="16" rx="1"/>
      <path d="M361 280 l12 9 l12 -9" fill="none" stroke="var(--icon-fill)" stroke-width="2"/>
      <text class="contact-text" x="413" y="294">marcus@kestrelfunding.com.au</text>
    </g>

    <!-- website -->
    <g class="contact-web">
      <circle class="icon-ring" cx="388" cy="354" r="25"/>
      <rect class="icon-line" x="377" y="351" width="14" height="8" rx="4" transform="rotate(-45 384 355)"/>
      <rect class="icon-line" x="385" y="349" width="14" height="8" rx="4" transform="rotate(-45 392 353)"/>
      <text class="contact-text" x="429" y="361">www.kestrelfunding.com.au</text>
    </g>
  </svg>
</main>
</body>
</html>
```